Tallow Ridge Snacks is looking for a wrapper design for our flagship protein bar. A sleek and simple, yet powerful design is a must. A company that has a no BS attitude, no flashy artwork and straight to the point advertising is key. Focusing on Bodybuilders and Powerlifters, the wrapper does not need to appeal to the mass market. A dark, simple, and powerful vibe must be achieved. Less is more

Target Market(s)

Body Builders and Powerlifters

Industry/Entity Type

Supplement

Font styles to use
Decorative

Colors

Designer to choose colors to be used in the design.

Requirements
Must have
• Refer to "Legal Label Requirements" document.
• Refer to "Template Drawn" or "Wrapper.ai" for dimensions.
• *Must have the "Tallow Bar" logo stamped somewhere on the front of the bar**
• Sleek and powerful design
• Neutral /dark colors and possible accents with logo colors (use sparingly)
• Flavor of bar "Peanut Butter Crisp" must be displayed somewhere. Simple graphic can be included if goes well with overall design.
• Wrapper will be foil, so please make use of metallic effects by leaving sections/outlines transparent.
• Claims: (State it uses "Hydrolyzed Whey Protein" and contains 25g's of protein and only 6g's of sugar, as well as only real ingredients (These must be in French as well)
• Proudly Canadian stamp with flag somewhere.
• Social Media Icons (Instagram,Facebook) as well as website "tallowbarsnx.ca)
• Design must be able to work with future bar flavors, with only altering colors/flavor graphic (if necessary)
• *Will Include Nutritional Label and Ingredient List at a later date*
Nice to have
• I think a cool graphic of a simple hand and hammer outline using the metallic effect would be cool. Something that resembles the act of "forging metal" while demonstrating power, but isn't too distracting.
• A label mock up to see a general bar idea
Should not have
• Flashy/godly designs

```html
<!DOCTYPE html>
<html lang="en">
<head>
<meta charset="UTF-8">
<title>Tallow Bar – Peanut Butter Crisp Wrapper</title>
<link rel="stylesheet" href="https://fonts.googleapis.com/css2?family=Bebas+Neue&display=swap">
<style>
  :root {
    --page-bg: #ffffff;
    --wrapper-dark: #2c2c2c;
    --wrapper-darker: #1f1f1f;
    --crimp-dark: #262626;
    --foil-light: #f2f2f2;
    --foil-mid: #c9c9cb;
    --foil-deep: #a9a9ad;
    --ink-light: #e4e4e4;
    --ink-dark: #2a2a2a;
    --accent-red: #ee3340;
    --badge-line: #3a3a3a;
  }
  * { margin: 0; padding: 0; box-sizing: border-box; }
  html, body {
    width: 1200px;
    height: 1000px;
    overflow: hidden;
    background: var(--page-bg);
  }
  .canvas {
    position: relative;
    width: 1200px;
    height: 1000px;
    font-family: "Bebas Neue", "Arial Narrow", sans-serif;
  }
  .wrapper-shape {
    position: absolute;
    left: 0;
    top: 0;
  }
  .brand-name {
    position: absolute;
    left: 292px;
    top: 398px;
    width: 310px;
    text-align: center;
    font-size: 64px;
    line-height: 1;
    letter-spacing: 10px;
    color: var(--ink-light);
  }
  .flavour-name {
    position: absolute;
    left: 307px;
    top: 522px;
    font-size: 36px;
    line-height: 1;
    letter-spacing: 0.5px;
    color: var(--ink-light);
  }
  .weight-band {
    position: absolute;
    left: 307px;
    top: 568px;
    width: 270px;
    height: 32px;
    background: var(--accent-red);
  }
  .weight-band span {
    position: absolute;
    left: 98px;
    top: 5px;
    font-size: 24px;
    line-height: 1;
    color: var(--ink-dark);
  }
  .hand-hammer-art {
    position: absolute;
    left: 742px;
    top: 398px;
    width: 172px;
    height: 206px;
    border-radius: 14px;
    background: linear-gradient(160deg, #3d3d3d 0%, #2a2a2a 60%, #5a5a5a 100%);
    opacity: 0.85;
  }
  .claim-badge {
    position: absolute;
    width: 74px;
    height: 74px;
    border: 2px solid var(--badge-line);
    border-radius: 50%;
    background: var(--foil-light);
    display: flex;
    flex-direction: column;
    align-items: center;
    justify-content: center;
    color: var(--ink-dark);
    text-align: center;
    line-height: 1;
  }
  .claim-badge .figure { font-size: 25px; }
  .claim-badge .label { font-size: 17px; margin-top: 2px; }
  .claim-badge .small { font-size: 12px; line-height: 1.15; }
  .badge-protein { left: 911px; top: 361px; }
  .badge-sugar { left: 911px; top: 456px; }
  .badge-whey { left: 911px; top: 548px; }
</style>
</head>
<body>
<div class="canvas">
  <svg class="wrapper-shape" width="1200" height="1000" viewBox="0 0 1200 1000" aria-hidden="true">
    <defs>
      <linearGradient id="bodyShade" x1="0" y1="0" x2="0" y2="1">
        <stop offset="0" stop-color="#3a3a3a"/>
        <stop offset="0.5" stop-color="#2e2e2e"/>
        <stop offset="1" stop-color="#1d1d1d"/>
      </linearGradient>
      <linearGradient id="foilSheen" x1="0" y1="0" x2="1" y2="1">
        <stop offset="0" stop-color="#b8b8bc"/>
        <stop offset="0.35" stop-color="#f4f4f4"/>
        <stop offset="0.7" stop-color="#d3d3d6"/>
        <stop offset="1" stop-color="#9d9da2"/>
      </linearGradient>
    </defs>
    <!-- left crimp -->
    <rect x="155" y="322" width="52" height="322" fill="var(--crimp-dark)"/>
    <!-- main body -->
    <rect x="200" y="338" width="855" height="294" fill="url(#bodyShade)"/>
    <!-- foil wedge -->
    <polygon points="858,338 1055,326 1055,648 695,632 740,560 810,450" fill="url(#foilSheen)"/>
    <!-- right crimp edge -->
    <rect x="1040" y="326" width="15" height="322" fill="#e6e6e8"/>
    <!-- radiating lines -->
    <g stroke="var(--badge-line)" stroke-width="3" stroke-linecap="round">
      <line x1="996" y1="398" x2="1048" y2="370"/>
      <line x1="1000" y1="432" x2="1052" y2="424"/>
      <line x1="1004" y1="476" x2="1050" y2="476"/>
      <line x1="1002" y1="520" x2="1050" y2="532"/>
      <line x1="1000" y1="560" x2="1048" y2="582"/>
      <line x1="996" y1="596" x2="1030" y2="622"/>
    </g>
  </svg>

  <div class="brand-name">Tallow Bar</div>

  <div class="flavour-name">Peanut Butter Crisp</div>
  <div class="weight-band"><span>50 G Bar</span></div>

  <div class="hand-hammer-art" role="img" aria-label="Silhouette of a fist gripping a forging hammer"></div>

  <div class="claim-badge badge-protein"><span class="figure">25 G</span><span class="label">Protein</span></div>
  <div class="claim-badge badge-sugar"><span class="figure">6 G</span><span class="label">Sugar</span></div>
  <div class="claim-badge badge-whey"><span class="small">Hydrolyzed<br>Whey</span></div>
</div>
</body>
</html>
```